Pediatric Pelvic Health Brochure

Looking to design a brochure for Marlow Brook's pelvic health program. I can provide imagery once I see the layout. Our website is marlowbrookpt.example so the look should reflect that

If you see PDF titled blue and word doc you will see what we provided as thoguhts.

Target Market(s)

parents of children

Industry/Entity Type

Health And Wellness

Font styles to use
Serif

Requirements
Must have
• clear call outs - easy to read with copy,
Should not have
• not look bland or dated

```html
<!DOCTYPE html>
<html lang="en">
<head>
<meta charset="utf-8">
<title>Marlow Brook's Pediatric Pelvic Health</title>
<link rel="stylesheet" href="https://fonts.googleapis.com/css2?family=Bebas+Neue&family=Tinos&display=swap">
<style>
  :root {
    --grey-light: #cfd3d6;
    --grey-mid: #b4b7ba;
    --grey-pale: #d9dbdc;
    --band-blue: #3f7fbd;
    --sky-top: #63c3f3;
    --sky-bottom: #3a6aa4;
    --icon-cyan: #35c6f2;
    --white: #ffffff;
  }
  html, body { margin: 0; padding: 0; overflow: hidden; }
  body { width: 1200px; height: 848px; background: var(--grey-light); }
  .spread { position: relative; width: 1200px; height: 848px; overflow: hidden; }
  .backdrop { position: absolute; inset: 0; }
  .heading {
    position: absolute; margin: 0; color: var(--white);
    font-family: "Bebas Neue", sans-serif; font-weight: 400;
    font-size: 35px; line-height: 34px; letter-spacing: 0.5px;
  }
  .heading-specialize { left: 101px; top: 420px; }
  .heading-diagnoses { left: 386px; top: 375px; }
  .swoosh {
    position: absolute; height: 14px;
    background: radial-gradient(ellipse at 35% 50%, rgba(20,40,70,0.55), rgba(20,40,70,0) 70%);
  }
  .swoosh-specialize { left: 112px; top: 460px; width: 170px; }
  .swoosh-diagnoses { left: 384px; top: 446px; width: 160px; }
  .swoosh-body { left: 44px; top: 818px; width: 170px; }
  .body-copy {
    position: absolute; left: 47px; width: 285px; margin: 0;
    color: var(--white); font-family: "Tinos", serif;
    font-size: 16.5px; line-height: 23px; text-align: justify; word-spacing: 2px;
  }
  .copy-first { top: 488px; }
  .copy-second { top: 671px; line-height: 24.5px; }
  .diagnosis-list { position: absolute; margin: 0; padding: 0; list-style: none; }
  .diagnosis-list li {
    position: absolute; left: 0; display: flex; align-items: flex-start; gap: 8px;
    color: var(--white); font-family: "Tinos", serif;
    font-size: 16.5px; line-height: 16px; word-spacing: 3px; letter-spacing: 0.3px;
  }
  .diagnosis-list svg { flex: none; width: 20px; height: 20px; margin-top: -3px; }
  .list-main { left: 386px; top: 0; width: 320px; }
  .list-side { left: 822px; top: 0; width: 300px; }
  .list-side li { gap: 14px; }
  .list-side svg { width: 30px; height: 30px; margin-top: -4px; }
</style>
</head>
<body>
<main class="spread">
  <svg class="backdrop" width="1200" height="848" viewBox="0 0 1200 848" aria-hidden="false">
    <defs>
      <linearGradient id="skyFill" x1="0" y1="0" x2="0" y2="1">
        <stop offset="0" stop-color="var(--sky-top)"/>
        <stop offset="1" stop-color="var(--sky-bottom)"/>
      </linearGradient>
      <radialGradient id="dishFill" cx="0.5" cy="0.45" r="0.55">
        <stop offset="0" stop-color="#8fb4c6"/>
        <stop offset="0.55" stop-color="#d4d9dc"/>
        <stop offset="1" stop-color="#e2e4e5"/>
      </radialGradient>
      <filter id="bandShadow" x="-5%" y="-5%" width="110%" height="120%">
        <feDropShadow dx="0" dy="3" stdDeviation="3" flood-color="#1a2a40" flood-opacity="0.45"/>
      </filter>
    </defs>
    <rect class="grey-panel-centre" x="365" y="0" width="427" height="520" fill="var(--grey-mid)"/>
    <rect class="grey-panel-right" x="792" y="0" width="408" height="520" fill="var(--grey-pale)"/>
    <g role="img" aria-label="Photo: assorted colourful capsules and tablets in a clear glass dish">
      <rect x="555" y="100" width="230" height="40" rx="6" fill="#d8dcde"/>
      <circle cx="857" cy="160" r="178" fill="url(#dishFill)"/>
    </g>
    <path class="band-outer" fill="var(--band-blue)" filter="url(#bandShadow)"
      d="M0,204 C150,300 420,300 546,110 C640,300 760,435 890,435 C1030,435 1130,370 1200,293 L1200,848 L0,848 Z"/>
    <path class="band-white" fill="var(--white)" filter="url(#bandShadow)"
      d="M0,262 C150,380 420,390 546,167 C650,380 770,502 910,502 C1050,502 1140,430 1200,355 L1200,848 L0,848 Z"/>
    <path class="band-body" fill="url(#skyFill)" filter="url(#bandShadow)"
      d="M0,308 C150,430 420,430 546,219 C660,430 790,548 920,548 C1060,548 1150,470 1200,400 L1200,848 L0,848 Z"/>
  </svg>

  <h2 class="heading heading-specialize">We Specialize</h2>
  <div class="swoosh swoosh-specialize"></div>
  <p class="body-copy copy-first">All pelvic physical therapy treatments are always done with a physical therapist trained in pediatric pelvic floor issues, and always with your doctor’s knowledge. Children are dressed and parents and guardians are present.</p>
  <p class="body-copy copy-second">During each session, your child or teen will work exclusively with one of our pelvic health physical therapists to help build strength, improve movement, and strengthen the skills</p>
  <div class="swoosh swoosh-body"></div>

  <h2 class="heading heading-diagnoses">We Treat a Range<br>of Diagnoses</h2>
  <div class="swoosh swoosh-diagnoses"></div>

  <ul class="diagnosis-list list-main">
    <li style="top:494px"><svg viewBox="0 0 20 20"><rect x="2" y="3" width="9" height="14" rx="2" fill="var(--icon-cyan)"/><rect x="13" y="3" width="5" height="8" rx="1" fill="var(--icon-cyan)"/></svg>Constipation</li>
    <li style="top:519px"><svg viewBox="0 0 20 20"><circle cx="5" cy="6" r="3" fill="var(--icon-cyan)"/><circle cx="15" cy="6" r="3" fill="var(--icon-cyan)"/><circle cx="10" cy="12" r="5" fill="var(--icon-cyan)"/></svg>Increased urinary frequency</li>
    <li style="top:551px"><svg viewBox="0 0 20 20"><path d="M8 2 A8 8 0 1 0 18 14 A7 7 0 0 1 8 2Z" fill="none" stroke="var(--icon-cyan)" stroke-width="1.5"/><circle cx="13" cy="11" r="4" fill="var(--icon-cyan)"/></svg>Night-time&nbsp; incontinence</li>
    <li style="top:580px"><svg viewBox="0 0 20 20"><rect x="1" y="8" width="18" height="7" rx="1" fill="none" stroke="var(--icon-cyan)" stroke-width="1.5"/><rect x="3" y="5" width="6" height="3" fill="var(--icon-cyan)"/><rect x="11" y="5" width="6" height="3" fill="var(--icon-cyan)"/><path d="M2 15v3M18 15v3" stroke="var(--icon-cyan)" stroke-width="1.5"/></svg>bed-wetting,&nbsp; or&nbsp; enuresis</li>
    <li style="top:608px"><svg viewBox="0 0 20 20"><circle cx="10" cy="10" r="6" fill="var(--icon-cyan)"/><path d="M10 1v4M10 15v4M1 10h4M15 10h4M4 4l3 3M13 13l3 3M16 4l-3 3M4 16l3-3" stroke="var(--icon-cyan)" stroke-width="2"/></svg>Day-time&nbsp; incontinence</li>
    <li style="top:637px"><svg viewBox="0 0 20 20"><circle cx="11" cy="9" r="8" fill="var(--icon-cyan)"/><path d="M4 14 L2 19 L8 16Z" fill="var(--icon-cyan)"/></svg>Giggle&nbsp; incontinence</li>
    <li style="top:663px"><svg viewBox="0 0 20 20"><circle cx="9" cy="6" r="4" fill="var(--icon-cyan)"/><rect x="4" y="10" width="12" height="9" rx="3" fill="var(--icon-cyan)"/></svg>Incontinence&nbsp; in&nbsp; the&nbsp; athletic&nbsp; female child&nbsp; or&nbsp; teenager</li>
    <li style="top:705px"><svg viewBox="0 0 20 20"><rect x="1" y="7" width="8" height="12" rx="1" fill="var(--icon-cyan)"/><rect x="11" y="9" width="8" height="10" fill="var(--icon-cyan)"/><rect x="13" y="2" width="3" height="7" fill="var(--icon-cyan)"/></svg>Waking&nbsp; up&nbsp; in&nbsp; the&nbsp; night&nbsp; to&nbsp; urinate&nbsp; or nocturia</li>
    <li style="top:746px"><svg viewBox="0 0 20 20"><rect x="2" y="1" width="16" height="4" fill="none" stroke="var(--icon-cyan)" stroke-width="1.5"/><path d="M3 5 L5 19 H15 L17 5" fill="none" stroke="var(--icon-cyan)" stroke-width="1.5"/><rect x="7" y="11" width="6" height="4" fill="none" stroke="var(--icon-cyan)" stroke-width="1.2"/></svg>Difficulty&nbsp; with&nbsp; urination:&nbsp; straining, slow&nbsp; flow,&nbsp; pain&nbsp; during&nbsp; or&nbsp; after urination</li>
  </ul>

  <ul class="diagnosis-list list-side">
    <li style="top:578px"><svg viewBox="0 0 30 30"><circle cx="9" cy="9" r="5" fill="none" stroke="var(--icon-cyan)" stroke-width="1.5"/><path d="M6 18 C12 14 18 22 24 18 M6 24 C12 20 18 28 24 24" fill="none" stroke="var(--icon-cyan)" stroke-width="1.5"/></svg>Reduced&nbsp; sensation&nbsp; of&nbsp; bladder&nbsp; or bowel&nbsp; fullness</li>
    <li style="top:620px"><svg viewBox="0 0 30 30"><circle cx="15" cy="15" r="11" fill="none" stroke="var(--icon-cyan)" stroke-width="1.5"/><path d="M10 12l3 2-3 2M20 12l-3 2 3 2M11 21 Q15 18 19 21" fill="none" stroke="var(--icon-cyan)" stroke-width="1.3"/></svg>Pain&nbsp; in&nbsp; the&nbsp; abdomen,&nbsp; bladder&nbsp; or lower&nbsp; back</li>
    <li style="top:665px"><svg viewBox="0 0 30 30"><path d="M15 3 L3 24 H15Z M15 3 L27 24 H15Z" fill="none" stroke="var(--icon-cyan)" stroke-width="1.5"/><ellipse cx="15" cy="25" rx="12" ry="3" fill="none" stroke="var(--icon-cyan)" stroke-width="1.5"/></svg>Fecal&nbsp; incontinence</li>
    <li style="top:704px"><svg viewBox="0 0 30 30"><rect x="7" y="4" width="16" height="22" rx="6" fill="none" stroke="var(--icon-cyan)" stroke-width="1.5"/><path d="M3 8v14M27 8v14M11 12h3M16 12h3M15 14v5" stroke="var(--icon-cyan)" stroke-width="1.3"/></svg>Treatment&nbsp; after&nbsp; pediatric&nbsp; pelvic surgeries</li>
  </ul>
</main>
</body>
</html>
```